Brivora Australia Company Values.

We have just completed our company purpose, beliefs and values (for the first time, we have not had these before)
We are now wanting to add images to each company value as a visual
so they are easily identified and understood for all our staff - we need them to remember the 5 Values.
We are a manufacturer of dental materials and infection control products, based in Melbourne.

What we would like:
- A Poster (that can be placed in our staff lunch rooms)
- The values to be lined up Horizontally
- Image on the top of the words
- Wording does not all need to be the same text font
- No image photographs - please use image graphics
- No images with people
- No dental related graphics

Target audience: Brivora staff

Our Values are:
Think Big
Have a go, learn and adapt
If you're gonna do it, do it bloody well
Empower Others
Be a good human

I have uploaded some examples.

Target Market(s)

Brivora Team members

Industry/Entity Type

Healthcare

Colors

Designer to choose colors to be used in the design.

Requirements
Must have
• Clear horizontal layout, space between each value
Should not have
• No images with humans or dental

```html
<!DOCTYPE html>
<html lang="en">
<head>
<meta charset="utf-8">
<title>Brivora Australia – Company Values</title>
<link rel="stylesheet" href="https://fonts.googleapis.com/css2?family=Titan+One&family=Poppins:ital,wght@1,800&family=Pacifico&family=Russo+One&family=Abril+Fatface&display=swap">
<style>
  :root {
    --paper: #ffffff;
    --orange: #fbaf15;
    --cyan: #22e6f2;
    --coral: #f2535e;
    --pink: #f9a3f0;
    --lime: #d4f562;
    --ink: #111111;
    --violet: #5a1fe6;
    --lavender: #9a6ad6;
    --white: #ffffff;
    --maroon: #7a1414;
    --gap: 12px;
  }
  * { margin: 0; padding: 0; box-sizing: border-box; }
  html, body { width: 849px; height: 1200px; overflow: hidden; background: var(--paper); }
  .values-poster {
    width: 849px; height: 1200px;
    display: flex; flex-direction: column; gap: var(--gap);
  }
  .value {
    flex: 1;
    display: flex; align-items: center;
    padding: 0 48px;
    position: relative;
  }
  .value--excellence { background: var(--orange); }
  .value--adapt { background: var(--cyan); }
  .value--human { background: var(--coral); }
  .value--big { background: var(--pink); }
  .value--empower { background: var(--lime); }

  .value-icon { width: 150px; height: 150px; flex: none; border-radius: 18px; }
  .value-text { flex: 1; text-align: center; }

  .value--excellence .value-icon { background: rgba(255,255,255,0.55); }
  .value--excellence .value-text {
    font-family: "Titan One", sans-serif;
    font-size: 37px; line-height: 1.12; color: var(--ink);
    text-transform: uppercase; padding-left: 40px;
  }

  .value--adapt .value-text {
    font-family: "Poppins", sans-serif; font-style: italic; font-weight: 800;
    font-size: 50px; line-height: 1.15; color: var(--violet);
    text-align: left; padding-left: 10px;
  }
  .value--adapt .value-icon { background: var(--lavender); }

  .value--human .value-icon { background: none; border-radius: 0; }
  .value--human .value-text {
    font-family: "Pacifico", cursive;
    font-size: 46px; line-height: 1.3; color: var(--white);
    padding-left: 40px;
  }

  .value--big .value-text {
    font-family: "Russo One", sans-serif; font-style: italic;
    font-size: 62px; color: var(--ink);
    text-align: left; padding-left: 10px;
  }
  .value--big .value-icon { background: rgba(60,20,60,0.25); }

  .value--empower .value-icon { background: rgba(20,20,20,0.2); }
  .value--empower .value-text {
    font-family: "Abril Fatface", serif;
    font-size: 60px; line-height: 1.08; color: var(--maroon);
    text-transform: uppercase; letter-spacing: 1px; padding-left: 40px;
  }
</style>
</head>
<body>
<main class="values-poster">
  <section class="value value--excellence">
    <div class="value-icon" role="img" aria-label="White line rocket flying to the right"></div>
    <h2 class="value-text">If you’re gonna<br>do it, do<br>it bloody well</h2>
  </section>

  <section class="value value--adapt">
    <h2 class="value-text">Have a go, learn<br>and adapt</h2>
    <div class="value-icon" role="img" aria-label="Purple jigsaw puzzle pieces fitting together"></div>
  </section>

  <section class="value value--human">
    <svg class="value-icon" viewBox="0 0 150 150" aria-hidden="true">
      <path d="M75 132 C40 104 10 80 10 50 C10 28 27 14 45 14 C60 14 70 24 75 34 C80 24 90 14 105 14 C123 14 140 28 140 50 C140 80 110 104 75 132 Z"
            fill="none" stroke="var(--white)" stroke-width="9" stroke-linejoin="round"/>
    </svg>
    <h2 class="value-text">Be a good<br>human</h2>
  </section>

  <section class="value value--big">
    <h2 class="value-text">Think Big</h2>
    <div class="value-icon" role="img" aria-label="Line drawing of a brain"></div>
  </section>

  <section class="value value--empower">
    <div class="value-icon" role="img" aria-label="Black line megaphone with sound lines"></div>
    <h2 class="value-text">Empower<br>Others</h2>
  </section>
</main>
</body>
</html>
```